Velvet Founders Income Blueprint

I need a Mockup Design for a digital course Materials - that is teaching you how to generate money with social media (e.G Glimmerly)
- we are two girls who are teaching but the design should be dark and neutral

- We need to get it same as the picture shows with Mockup
BOX and Thumbnail
- We don't have a real logo yet so it needs to all included with the package design. This designs becomes also the logo in a way.

- It needs to be classy and luxury and shows a BOLD Brand
- we like it very black and dark - mixed with gold
-

Women and Men who want to escape the 9/5

```html
<!DOCTYPE html>
<html lang="en">
<head>
<meta charset="UTF-8">
<title>Velvet Founders Income Blueprint – Course Box Front</title>
<link rel="stylesheet" href="https://fonts.googleapis.com/css2?family=Montserrat:wght@500;700&family=Yellowtail&display=swap">
<style>
  :root {
    --canvas-bg: #e7e7e9;
    --box-black: #151515;
    --box-black-soft: #232323;
    --gold-light: #f3d46a;
    --gold-mid: #d6a531;
    --gold-deep: #8a5a18;
    --script-white: #f4f4f4;
  }
  * { margin: 0; padding: 0; box-sizing: border-box; }
  html, body {
    width: 1200px;
    height: 1200px;
    overflow: hidden;
    background: var(--canvas-bg);
  }
  .canvas {
    position: relative;
    width: 1200px;
    height: 1200px;
    background: var(--canvas-bg);
  }
  .box-front {
    position: absolute;
    left: 288px;
    top: 70px;
    width: 625px;
    height: 1000px;
    background:
      linear-gradient(115deg, transparent 0 18%, rgba(255,255,255,0.05) 18% 30%, transparent 30% 44%, rgba(255,255,255,0.06) 44% 56%, transparent 56% 70%, rgba(255,255,255,0.04) 70% 82%, transparent 82%),
      linear-gradient(160deg, var(--box-black-soft), var(--box-black) 60%);
    overflow: hidden;
    box-shadow: 0 20px 40px rgba(0,0,0,0.18);
  }
  .brand {
    position: absolute;
    top: 70px;
    left: 0;
    width: 100%;
    text-align: center;
  }
  .brand-mark {
    display: block;
    margin: 0 auto 30px;
    width: 120px;
    height: 120px;
  }
  .brand-name {
    font-family: "Montserrat", sans-serif;
    font-weight: 500;
    font-size: 27px;
    letter-spacing: 0.22em;
    color: var(--gold-mid);
  }
  .title {
    position: absolute;
    top: 410px;
    left: 0;
    width: 100%;
    text-align: center;
  }
  .title-line {
    display: block;
    font-family: "Montserrat", sans-serif;
    font-weight: 700;
    font-size: 60px;
    line-height: 58px;
    letter-spacing: 0.01em;
    background: linear-gradient(180deg, var(--gold-light) 0%, var(--gold-mid) 55%, var(--gold-deep) 100%);
    -webkit-background-clip: text;
    background-clip: text;
    color: transparent;
  }
  .title-script {
    display: block;
    position: relative;
    z-index: 2;
    margin: -18px 0 -14px;
    font-family: "Yellowtail", cursive;
    font-size: 74px;
    line-height: 80px;
    color: var(--script-white);
    transform: rotate(-4deg);
  }
  .platform {
    position: absolute;
    top: 690px;
    left: 50%;
    width: 220px;
    height: 170px;
    transform: translateX(-50%);
    border-radius: 18px;
    background: radial-gradient(circle at center, rgba(214,165,49,0.55), rgba(138,90,24,0.25) 55%, transparent 75%);
  }
  .platform-label {
    position: absolute;
    top: 880px;
    left: 0;
    width: 100%;
    text-align: center;
    font-family: "Montserrat", sans-serif;
    font-weight: 500;
    font-size: 18px;
    letter-spacing: 0.2em;
    color: var(--gold-mid);
  }
  .gold-band {
    position: absolute;
    left: 0;
    bottom: 0;
    width: 100%;
    height: 60px;
    background: linear-gradient(90deg, var(--gold-mid) 0%, var(--gold-light) 22%, var(--gold-deep) 50%, var(--gold-mid) 78%, var(--gold-light) 100%);
  }
</style>
</head>
<body>
  <main class="canvas">
    <section class="box-front">
      <header class="brand">
        <svg class="brand-mark" viewBox="0 0 120 120" aria-hidden="true">
          <circle cx="60" cy="60" r="54" fill="none" stroke="#d6a531" stroke-width="4"/>
        </svg>
        <p class="brand-name">LENA VARO</p>
      </header>

      <h1 class="title">
        <span class="title-line">VELVET</span>
        <span class="title-line">FOUNDERS</span>
        <span class="title-script">Income</span>
        <span class="title-line">BLUEPRINT</span>
      </h1>

      <div class="platform" role="img" aria-label="Gold circuit-chip illustration representing the Glimmerly social platform"></div>
      <p class="platform-label">GLIMMERLY</p>

      <div class="gold-band"></div>
    </section>
  </main>
</body>
</html>
```